Simple Banners for several sites

I'm looking for banners in the following formats for the sites listed bellow:

* Leaderboard
* Wide Skyscraper
* Skyscaper
* Square Button
* Micro bar
* Full banner
* Half Banner
* Medium Rectangle

The websites:
* http://notavault.crenmop.com/
* http://quolet.com/
* http://dravimunto.com/

I would like to get 1 sets of banners for each website, and I'ld like you to submit each set/site independently.

```html
<!DOCTYPE html>
<html lang="en">
<head>
<meta charset="utf-8">
<title>Not A Vault – Banner Set</title>
<link rel="stylesheet" href="https://fonts.googleapis.com/css2?family=Arimo:wght@400;700&family=Didact+Gothic&display=swap">
<style>
  :root {
    --backdrop: #ece6df;
    --banner-bg: #ffffff;
    --brand-green: #5a9e3a;
    --button-green: #5f9f45;
    --ink: #111111;
    --art-warm: #e9d7a6;
    --art-cool: #9fb4b3;
    --art-deep: #6f8a8c;
  }
  * { box-sizing: border-box; margin: 0; padding: 0; }
  html, body { width: 1200px; height: 900px; overflow: hidden; }
  body {
    background: var(--backdrop);
    font-family: "Arimo", Arial, sans-serif;
    color: var(--ink);
    position: relative;
  }
  .banner {
    position: absolute;
    background: var(--banner-bg);
    overflow: hidden;
  }
  .brand-name {
    position: absolute;
    font-family: "Didact Gothic", "Arimo", sans-serif;
    color: var(--brand-green);
    white-space: nowrap;
    letter-spacing: -0.5px;
  }
  .tagline {
    position: absolute;
    font-weight: 700;
    text-align: center;
    white-space: nowrap;
  }
  .tagline .accent { color: var(--brand-green); }
  .illustration {
    position: absolute;
    background: linear-gradient(100deg, var(--art-warm) 0%, var(--art-cool) 45%, var(--art-deep) 100%);
  }
  .cta-button {
    position: absolute;
    background: var(--button-green);
    color: #fff;
    border-radius: 999px;
    font-weight: 700;
    display: flex;
    align-items: center;
    justify-content: center;
    letter-spacing: -0.3px;
  }
  .site-url {
    position: absolute;
    font-weight: 700;
    font-size: 11px;
    white-space: nowrap;
  }

  /* Leaderboard */
  .leaderboard { left: 221px; top: 48px; width: 853px; height: 105px; }
  .leaderboard .illustration { left: 0; top: 0; width: 265px; height: 105px; }
  .leaderboard .tagline { left: 275px; top: 23px; width: 400px; font-size: 23px; line-height: 30px; }
  .leaderboard .brand-name { right: 6px; top: 2px; font-size: 31px; }
  .leaderboard .cta-button { left: 694px; top: 48px; width: 148px; height: 37px; font-size: 20px; }
  .leaderboard .site-url { right: 4px; top: 85px; }

  /* Medium rectangle */
  .rectangle { left: 296px; top: 305px; width: 352px; height: 293px; }
  .rectangle .brand-name { left: 0; width: 100%; text-align: center; top: 2px; font-size: 31px; }
  .rectangle .tagline { left: 0; width: 100%; top: 42px; font-size: 23px; line-height: 31px; }
  .rectangle .illustration { left: 0; top: 105px; width: 310px; height: 188px; }
  .rectangle .cta-button { left: 204px; top: 223px; width: 130px; height: 35px; font-size: 19px; }
  .rectangle .site-url { right: 10px; top: 263px; }

  /* Skyscraper */
  .skyscraper { left: 786px; top: 176px; width: 187px; height: 703px; }
  .skyscraper .brand-name { left: 0; width: 100%; text-align: center; top: 36px; font-size: 38px; }
  .skyscraper .illustration { left: 0; top: 127px; width: 187px; height: 178px; }
  .skyscraper .tagline { left: 0; width: 100%; top: 358px; font-size: 25px; line-height: 34px; }
  .skyscraper .cta-button { left: 26px; top: 610px; width: 146px; height: 39px; font-size: 21px; }
  .skyscraper .site-url { left: 0; width: 100%; text-align: center; top: 653px; }
</style>
</head>
<body>

  <section class="banner leaderboard" aria-label="Leaderboard banner">
    <div class="illustration" role="img" aria-label="Illustration of a person typing at a very long computer stuffed with web pages"></div>
    <p class="tagline">All the Info from the Internet,<br><span class="accent">DUMPED</span> in a simple <span class="accent">SITE</span></p>
    <p class="brand-name">Not A Vault</p>
    <div class="cta-button">CLICK HERE</div>
    <p class="site-url">www.notavault.crenmop.com</p>
  </section>

  <section class="banner rectangle" aria-label="Medium rectangle banner">
    <p class="brand-name">Not A Vault</p>
    <p class="tagline">All the Info from the Internet,<br><span class="accent">DUMPED</span> in a simple <span class="accent">SITE</span></p>
    <div class="illustration" role="img" aria-label="Illustration of a person typing at a very long computer stuffed with web pages"></div>
    <div class="cta-button">CLICK HERE</div>
    <p class="site-url">www.notavault.crenmop.com</p>
  </section>

  <section class="banner skyscraper" aria-label="Skyscraper banner">
    <p class="brand-name">Not A Vault</p>
    <div class="illustration" role="img" aria-label="Illustration of a person typing at a very long computer stuffed with web pages"></div>
    <p class="tagline">All the Info<br>from the<br>Internet,<br><span class="accent">DUMPED</span><br>in a<br>simple <span class="accent">SITE</span></p>
    <div class="cta-button">CLICK HERE</div>
    <p class="site-url">www.notavault.crenmop.com</p>
  </section>

</body>
</html>
```